Simple Business Cards for Self-employed Coach

Simple business card with a design that includes the QRT logo.
Using either only the logo color or additional colors that match the logo.

Integral Coaches reach deeply into the past, gathering wisdom from East and West, while still staying current with the frontiers of new discovery in cognitive science, genetics, and other disciplines. see https://www.brightharborpath.example/what-is-integral-coaching/

Target Market(s)

Coaching Clients in Tokyo /Asia; in business organizations, but also outside

Industry/Entity Type

Life Coaching

Contact Information for Business Card

Tobias Reinholt
Certified Pathway Coach

4-2-28 Hanamidori
Setagaya 163-0442
Tokyo, Japan

Phone: +81 70 4813 9027
E-Mail: tobias.reinholt@mailvessel.example

Font styles to use
Sans Serif

Colors
00a990

Requirements
Must have
• include uploaded logo
• color fitting with QRT logo color
Nice to have
• simple, elegant design
Should not have
• clutter

```html
<!DOCTYPE html>
<html lang="en">
<head>
<meta charset="utf-8">
<title>QRT Pathway Coach – Business Cards</title>
<link rel="stylesheet" href="https://fonts.googleapis.com/css2?family=Lato:wght@400;700&display=swap">
<style>
  :root {
    --teal: #00897a;
    --teal-bright: #00a990;
    --ink: #4a4a4a;
    --paper: #ffffff;
    --paper-shade: #f1f3f3;
    --backdrop: #2b2b2b;
  }
  html, body {
    margin: 0;
    width: 1200px;
    height: 997px;
    overflow: hidden;
    background: var(--backdrop);
    font-family: "Lato", Arial, sans-serif;
  }
  .card {
    position: absolute;
    width: 560px;
    height: 320px;
    border-radius: 16px;
    background: linear-gradient(135deg, var(--paper) 55%, var(--paper-shade));
    overflow: hidden;
    box-shadow: 0 18px 40px rgba(0,0,0,.45);
  }
  .card--contact { left: 80px; top: 110px; }
  .card--front { left: 560px; top: 500px; }

  .brand {
    position: absolute;
    left: 0; right: 0;
    display: flex;
    justify-content: center;
    align-items: center;
    gap: 12px;
    color: var(--teal);
    font-weight: 700;
    letter-spacing: 0.18em;
  }
  .brand-square { background: var(--teal); display: block; }
  .card--contact .brand { top: 28px; font-size: 40px; }
  .card--contact .brand-square { width: 26px; height: 26px; }
  .card--front .brand { top: 70px; font-size: 72px; }
  .card--front .brand-square { width: 46px; height: 46px; }

  .name-band {
    position: absolute;
    left: 0; right: 0; top: 118px;
    height: 36px;
    background: var(--teal);
    color: var(--paper);
    font-size: 21px;
    line-height: 36px;
    text-align: center;
  }
  .role {
    position: absolute;
    left: 0; right: 0; top: 162px;
    text-align: center;
    font-size: 14px;
    color: var(--ink);
  }
  .contact-list {
    position: absolute;
    left: 26px; top: 214px;
    margin: 0; padding: 0;
    list-style: none;
    font-size: 14px;
    color: var(--ink);
  }
  .contact-list li { display: flex; align-items: center; gap: 10px; margin-bottom: 8px; }
  .contact-list svg { width: 14px; height: 14px; fill: var(--teal); flex: none; }
  .address {
    position: absolute;
    right: 26px; top: 204px;
    margin: 0;
    text-align: right;
    font-style: normal;
    font-size: 13px;
    line-height: 1.45;
    color: var(--ink);
  }
  .welcome-band {
    position: absolute;
    left: 0; right: 0; bottom: 0;
    height: 36px;
    background: var(--teal);
    color: var(--paper);
    font-size: 13px;
    line-height: 36px;
    text-align: center;
  }

  .web-band {
    position: absolute;
    right: 0; top: 196px;
    width: 380px;
    height: 40px;
    background: var(--teal);
    clip-path: polygon(40px 0, 100% 0, 100% 100%, 0 100%);
    color: var(--paper);
    font-size: 16px;
    font-weight: 700;
    letter-spacing: 0.16em;
    line-height: 40px;
    text-align: right;
    padding-right: 20px;
    box-sizing: border-box;
  }
  .find-coach {
    position: absolute;
    left: 30px; top: 246px;
    color: var(--teal);
    font-size: 22px;
    font-weight: 700;
    letter-spacing: 0.04em;
  }
  .rule {
    position: absolute;
    left: 0; right: 0; top: 236px;
    height: 2px;
    background: var(--teal);
  }
  .rule--lower { top: 284px; height: 1px; width: 260px; }
</style>
</head>
<body>

<article class="card card--contact">
  <div class="brand"><span class="brand-square"></span><span>QRT</span></div>
  <div class="name-band">Tobias Reinholt</div>
  <div class="role">Certified Pathway Coach</div>
  <ul class="contact-list">
    <li>
      <svg viewBox="0 0 24 24" aria-hidden="true"><path d="M6.6 10.8a15.1 15.1 0 0 0 6.6 6.6l2.2-2.2a1 1 0 0 1 1-.25 11.4 11.4 0 0 0 3.6.57 1 1 0 0 1 1 1V20a1 1 0 0 1-1 1A17 17 0 0 1 3 4a1 1 0 0 1 1-1h3.5a1 1 0 0 1 1 1c0 1.25.2 2.45.57 3.57a1 1 0 0 1-.25 1z"/></svg>
      +81 70 4813 9027
    </li>
    <li>
      <svg viewBox="0 0 24 24" aria-hidden="true"><path d="M2 5h20L12 12.5zM2 7l10 8 10-8v12H2z"/></svg>
      tobias.reinholt@mailvessel.example
    </li>
  </ul>
  <address class="address">
    4-2-28 Hanamidori<br>
    Setagaya 163-0442, Tokyo, Japan
  </address>
  <div class="welcome-band">We welcome your questions &amp; comments about our work. Feel free to contact us</div>
</article>

<article class="card card--front">
  <div class="brand"><span class="brand-square"></span><span>QRT</span></div>
  <div class="web-band">www.brightharborpath.example</div>
  <div class="rule"></div>
  <div class="find-coach">FIND A COACH</div>
  <div class="rule rule--lower"></div>
</article>

</body>
</html>
```